Business cards for Wendcycle

We need a business card layout for our new bike and e-bike rental (we also sell used e-bikes and bike accessories). The logo already exists.

```html
<!DOCTYPE html>
<html lang="en">
<head>
<meta charset="utf-8">
<title>Wendcycle business cards</title>
<link rel="stylesheet" href="https://fonts.googleapis.com/css2?family=Fira+Sans:wght@300;400;500;600&display=swap">
<style>
  :root {
    --backdrop: #e6e6e6;
    --ink-dark: #232d34;
    --teal: #3aaa8c;
    --paper: #f6f6f5;
    --text: #2b3238;
    --muted-light: #e9ecec;
    --mark-area: #dfe3e3;
  }
  * { margin: 0; padding: 0; box-sizing: border-box; }
  html, body {
    width: 1200px; height: 576px; overflow: hidden;
    background: var(--backdrop);
    font-family: "Fira Sans", sans-serif;
  }
  .stage { position: relative; width: 1200px; height: 576px; }
  .card {
    position: absolute; top: 138px;
    width: 484px; height: 294px;
    border-radius: 13px; overflow: hidden;
    box-shadow: 0 3px 6px rgba(0,0,0,0.18);
  }
  /* front */
  .card-front { left: 82px; background: var(--ink-dark); }
  .front-brand {
    position: absolute; left: 0; right: 0; top: 96px;
    text-align: center; color: var(--teal);
    font-weight: 300; font-size: 64px; letter-spacing: 1px; line-height: 1;
  }
  .front-tagline {
    position: absolute; left: 0; right: 0; top: 172px;
    text-align: center; color: var(--muted-light);
    font-weight: 400; font-size: 16px; line-height: 1;
  }
  /* back */
  .card-back { left: 602px; background: var(--paper); color: var(--text); }
  .edge-tab {
    position: absolute; left: -14px; top: 30px;
    width: 28px; height: 56px; border-radius: 0 28px 28px 0;
    background: var(--teal);
  }
  .holder-name {
    position: absolute; left: 23px; top: 38px;
    color: var(--teal); font-weight: 600; font-size: 18px; line-height: 1;
  }
  .holder-role {
    position: absolute; left: 23px; top: 60px;
    font-size: 11px; font-weight: 400; line-height: 1;
  }
  .back-brand {
    position: absolute; right: 36px; top: 30px; text-align: center;
  }
  .back-brand-name {
    color: var(--teal); font-weight: 300; font-size: 44px; line-height: 1; letter-spacing: 0.5px;
  }
  .back-brand-tagline {
    margin-top: 5px; font-size: 12px; font-weight: 500; line-height: 1;
  }
  .address {
    position: absolute; left: 23px; top: 172px;
    font-size: 12.5px; line-height: 18px; font-weight: 400; font-style: normal;
  }
  .contact-list {
    position: absolute; left: 23px; top: 216px; list-style: none;
    font-size: 12.5px; line-height: 17px;
  }
  .contact-list li { display: flex; align-items: center; gap: 14px; }
  .contact-icon { width: 10px; height: 10px; fill: var(--teal); flex: none; }
  .mark-area {
    position: absolute; right: 0; bottom: 0;
    width: 214px; height: 166px;
    background: linear-gradient(135deg, var(--paper), var(--mark-area));
  }
</style>
</head>
<body>
<main class="stage">
  <section class="card card-front" aria-label="Card front">
    <div class="front-brand">WENDCYCLE</div>
    <div class="front-tagline">ride easy, ride far</div>
  </section>

  <section class="card card-back" aria-label="Card back">
    <span class="edge-tab"></span>
    <div class="holder-name">Lena Hartwig</div>
    <div class="holder-role">Managing Director</div>

    <div class="back-brand">
      <div class="back-brand-name">WENDCYCLE</div>
      <div class="back-brand-tagline">ride easy, ride far</div>
    </div>

    <address class="address">
      18 Lindenweg, Riverside,<br>
      Greenfield, US 482019
    </address>

    <ul class="contact-list">
      <li>
        <svg class="contact-icon" viewBox="0 0 10 10" aria-hidden="true"><path d="M1 2.5C1 1.5 2.5 1 5 1s4 .5 4 1.5v1H7V2.8H3v.7H1z M2 4h6l1 5H1z"/></svg>
        555.204.7718
      </li>
      <li>
        <svg class="contact-icon" viewBox="0 0 10 10" aria-hidden="true"><path d="M0 2h10v6H0z M0.8 2.6 5 5.6l4.2-3v.9L5 6.5.8 3.5z" fill-rule="evenodd"/></svg>
        lena@wendcycle.com
      </li>
      <li>
        <svg class="contact-icon" viewBox="0 0 10 10" aria-hidden="true"><circle cx="5" cy="5" r="4.5"/><path d="M0.5 5h9M5 .5v9M5 .5c-2 2.5-2 6.5 0 9M5 .5c2 2.5 2 6.5 0 9" stroke="#f6f6f5" stroke-width="0.7" fill="none"/></svg>
        www.wendcycle.com
      </li>
    </ul>

    <div class="mark-area" role="img" aria-label="Brand bicycle emblem area"></div>
  </section>
</main>
</body>
</html>
```